Process Roadmap for Interior Design Firm

We are looking to ramp up the design appeal of our current process roadmap to be very visually interesting, while staying informative and descriptive about our process.

Target Market(s)

In-house Clients

Industry/Entity Type

Interior Design Firm focused on sustainable and holistic design.

Other font styles liked:
• raleway

Requirements
Must have
• 1.) it would be nice if the graphic provided a more clear indication of the “journey” from one step to the next, so that there was a clear sense of the progression (such that we are directing the viewer) 2.). We would want it to fit on an 8.5”x11” page (the page could be horizontal when we have the Steady Pathway formatted out with the testimonials) (in addition to the testimonials, we may also want to have the detailed descriptions of each step of the process presented below the graphic, so that the graphic is cleaner) 3.) ideally the graphic is clear and simple enough to also be used on our Bi-Weekly Client Updates, which will be typed updates for clients re their project budgets, schedule and scope. The Steady Pathway graphic (without all the testimonials) would be at the end of the update, and would fit on the page horizontally at the bottom, perhaps in a space which is 7.5”w x 4”h or so.
Should not have
• bold or bright colors. Natural neutrals are preferred, such as the ones featured on the provided graphic.

```html
<!DOCTYPE html>
<html lang="en">
<head>
<meta charset="utf-8">
<title>HMD Steady Pathway</title>
<link href="https://fonts.googleapis.com/css2?family=Barlow:wght@400;600&display=swap" rel="stylesheet">
<style>
  :root {
    --sand: #c2b49a;
    --sand-deep: #b5a687;
    --sand-light: #d6ccba;
    --cream: #f5f3f0;
    --panel: #f1ede8;
    --white: #ffffff;
  }
  * { box-sizing: border-box; margin: 0; padding: 0; }
  html, body { width: 1200px; height: 927px; overflow: hidden; background: var(--white); }
  body { font-family: "Barlow", sans-serif; position: relative; }

  .roadmap-band { position: absolute; left: 0; top: 0; width: 1200px; height: 659px; background: var(--sand); }

  .brand-card {
    position: absolute; left: 40px; top: 41px; width: 129px; height: 58px;
    background: var(--white); border-radius: 8px; overflow: hidden;
    display: flex; align-items: center;
  }
  .brand-card .brand-square { width: 24px; height: 58px; background: var(--sand-light); flex: none; }
  .brand-card .brand-name {
    flex: 1; text-align: center; color: var(--sand-deep);
    font-size: 12px; font-weight: 400; letter-spacing: 1.5px; line-height: 1.2; text-transform: uppercase;
  }

  .title-bar {
    position: absolute; left: 195px; top: 41px; width: 981px; height: 58px; border-radius: 8px 0 0 8px;
    background: linear-gradient(90deg, var(--white) 0%, #f7f5f2 35%, rgba(255,255,255,0.2) 85%, rgba(255,255,255,0) 100%);
    display: flex; align-items: center; justify-content: center;
  }
  .title-bar h1 { font-size: 25px; font-weight: 600; color: var(--sand-deep); letter-spacing: 0.2px; }

  .timeline-art { position: absolute; left: 0; top: 0; }

  .step {
    position: absolute; width: 95px; height: 95px; border-radius: 50%;
    background: var(--cream); display: flex; align-items: center; justify-content: center;
    font-size: 15.5px; font-weight: 600; color: var(--sand);
  }
  .step.up { top: 262px; }
  .step.down { top: 401px; }

  .note {
    position: absolute; width: 187px; color: var(--white);
    font-size: 13px; line-height: 16.6px; text-align: center; padding: 0 12px;
  }
  .note p + p { margin-top: 8px; }
  .note.above { top: 143px; height: 195px; display: flex; flex-direction: column; justify-content: flex-end; padding-bottom: 18px; }
  .note.below { top: 437px; }

  .testimonials {
    position: absolute; left: 40px; top: 709px; width: 1121px; height: 176px;
    background: var(--panel); border-radius: 18px;
  }
  .testimonials-label {
    position: absolute; left: 537px; top: 691px; width: 125px; height: 34px;
    background: var(--sand); border-radius: 10px; color: var(--white);
    font-size: 17px; font-weight: 600; display: flex; align-items: center; justify-content: center;
  }
  .quote {
    position: absolute; top: 746px; width: 180px; text-align: center;
    font-size: 16.5px; line-height: 20.6px; color: var(--sand-deep);
  }
  .quote-divider {
    position: absolute; top: 769px; height: 72px; border-left: 2px dashed var(--sand-light);
  }
</style>
</head>
<body>
  <div class="roadmap-band"></div>

  <div class="brand-card">
    <span class="brand-square"></span>
    <span class="brand-name">Hale Marsh<br>Design</span>
  </div>

  <div class="title-bar"><h1>HMD Steady Pathway</h1></div>

  <svg class="timeline-art" width="1200" height="659" viewBox="0 0 1200 659">
    <defs>
      <linearGradient id="fade-up" x1="0" y1="0" x2="0" y2="1">
        <stop offset="0" stop-color="#d6ccba" stop-opacity="0.05"/>
        <stop offset="1" stop-color="#d6ccba" stop-opacity="0.95"/>
      </linearGradient>
      <linearGradient id="fade-down" x1="0" y1="0" x2="0" y2="1">
        <stop offset="0" stop-color="#d6ccba" stop-opacity="0.95"/>
        <stop offset="1" stop-color="#d6ccba" stop-opacity="0"/>
      </linearGradient>
      <path id="bubble-above" d="M12,143 H175 Q187,143 187,155 V326 Q187,338 175,338 H103.5 L93.5,356 L83.5,338 H12 Q0,338 0,326 V155 Q0,143 12,143 Z"/>
      <path id="bubble-below" d="M12,419 H83.5 L93.5,401 L103.5,419 H175 Q187,419 187,431 V615 H0 V431 Q0,419 12,419 Z"/>
    </defs>

    <g fill="url(#fade-up)">
      <use href="#bubble-above" x="195"/>
      <use href="#bubble-above" x="506.5"/>
      <use href="#bubble-above" x="818"/>
    </g>
    <g fill="url(#fade-down)">
      <use href="#bubble-below" x="39.5"/>
      <use href="#bubble-below" x="351"/>
      <use href="#bubble-below" x="662"/>
      <use href="#bubble-below" x="973.5"/>
    </g>

    <line x1="38" y1="378.5" x2="1162" y2="378.5" stroke="#dcd3c3" stroke-width="1.6" stroke-dasharray="5 4"/>

    <g stroke="#dcd3c3" stroke-width="1.6">
      <line x1="133" y1="357" x2="133" y2="378"/>
      <line x1="288.5" y1="378" x2="288.5" y2="401"/>
      <line x1="444" y1="357" x2="444" y2="378"/>
      <line x1="600" y1="378" x2="600" y2="401"/>
      <line x1="755.5" y1="357" x2="755.5" y2="378"/>
      <line x1="911" y1="378" x2="911" y2="401"/>
      <line x1="1066.5" y1="357" x2="1066.5" y2="378"/>
    </g>
    <g fill="#dcd3c3">
      <circle cx="133" cy="378.5" r="4.5"/>
      <circle cx="288.5" cy="378.5" r="4.5"/>
      <circle cx="444" cy="378.5" r="4.5"/>
      <circle cx="600" cy="378.5" r="4.5"/>
      <circle cx="755.5" cy="378.5" r="4.5"/>
      <circle cx="911" cy="378.5" r="4.5"/>
      <circle cx="1066.5" cy="378.5" r="4.5"/>
    </g>
  </svg>

  <div class="step up" style="left:85.5px">Listening</div>
  <div class="step down" style="left:241px">Visioning</div>
  <div class="step up" style="left:396.5px">Planning</div>
  <div class="step down" style="left:552.5px">Designing</div>
  <div class="step up" style="left:708px">Managing</div>
  <div class="step down" style="left:863.5px">Installing</div>
  <div class="step up" style="left:1019px">Completing</div>

  <div class="note above" style="left:195px">
    <p>Facilitating a guided visioning process to clarify the deepest intention, true purpose, and highest potential for their home and their future within it.</p>
  </div>
  <div class="note above" style="left:506.5px">
    <p>Following the schedule through the design phases from initial design concepts, technical drawings and details, and the selection of all finishes, fixtures, and surnishings.</p>
  </div>
  <div class="note above" style="left:818px">
    <p>Overseeing the inspection, installation, and arrangement of all furnishings, lighting, artwork, and decorative items.</p>
    <p>Taking care of every last detail.</p>
  </div>

  <div class="note below" style="left:39.5px">
    <p>Listening to our clients, their land, and their home.</p>
    <p style="margin-top:17px">Identifying their needs, challenges, wishes, and dreams.</p>
  </div>
  <div class="note below" style="left:351px">
    <p>Turning our client's vision into a clearly defined scope., budget, and timeline.</p>
    <p>Mapping out the steps for making their dream a reality.</p>
    <p>Setting a meeting schedule from start to finish.</p>
  </div>
  <div class="note below" style="left:662px">
    <p>Coordinating with clients, builders, architects, and vendors to ensure that the design is executed with excellence, and the construction and furnishings are on-time and on-budget.</p>
  </div>
  <div class="note below" style="left:973.5px">
    <p>Fixing any issues or defects.</p>
    <p>Follow up on all remaining items.</p>
    <p>Completing the final finishing touches to our client's full and total satisfaction.</p>
  </div>

  <div class="testimonials"></div>
  <div class="testimonials-label">Testimonials</div>

  <p class="quote" style="left:90px">Nora to send over testimonials for fill this space - three or four columns of testimonials</p>
  <span class="quote-divider" style="left:319px"></span>
  <p class="quote" style="left:369px">Nora to send over testimonials for fill this space - three or four columns of testimonials</p>
  <span class="quote-divider" style="left:599px"></span>
  <p class="quote" style="left:649px">Nora to send over testimonials for fill this space - three or four columns of testimonials</p>
  <span class="quote-divider" style="left:879px"></span>
  <p class="quote" style="left:929px">Nora to send over testimonials for fill this space - three or four columns of testimonials</p>
</body>
</html>
```